TBV business card

For a business card with our logo

Contact Information for Business Card

Lucien MARVET
Founder & CEO
email : ceo@brightlanternstudio.com / www.brightlanternstudio.com /
instagram / facebook / WhatsApp
N°: +590 690 482 517

Colors

Designer to choose colors to be used in the design.

```html
<!DOCTYPE html>
<html lang="en">
<head>
<meta charset="utf-8">
<title>TBV business card</title>
<link rel="stylesheet" href="https://fonts.googleapis.com/css2?family=EB+Garamond:wght@400;600&display=swap">
<style>
  :root {
    --stage: #1c1c1e;
    --card-white: #ffffff;
    --card-black: #0f0f10;
    --emboss: #1b1b1d;
    --brand-blue: #0d56a6;
    --brand-orange: #ef7324;
    --ink: #1d1d1f;
  }
  * { box-sizing: border-box; margin: 0; padding: 0; }
  html, body { width: 1200px; height: 1200px; overflow: hidden; }
  body {
    background: var(--stage);
    font-family: "EB Garamond", Georgia, serif;
    position: relative;
  }
  .card {
    position: absolute;
    left: 240px;
    width: 720px;
    height: 412px;
    border-radius: 26px;
    overflow: hidden;
    box-shadow: 0 18px 40px rgba(0,0,0,.55);
  }
  /* back side */
  .card-back { top: 130px; background: var(--card-black); }
  .back-mark {
    position: absolute; inset: 0;
    display: flex; flex-direction: column; align-items: center; justify-content: center; gap: 18px;
  }
  .back-mark .mark-dot { width: 120px; height: 120px; border-radius: 50%; background: var(--emboss); }
  .back-mark .mark-name { color: var(--emboss); font-size: 34px; letter-spacing: 2px; font-weight: 600; }

  /* front side */
  .card-front { top: 660px; background: var(--card-white); }
  .front-band { position: absolute; left: 0; bottom: 0; width: 720px; height: 412px; }
  .brand {
    position: absolute; left: 44px; top: 110px; width: 286px;
    display: flex; flex-direction: column; align-items: center; gap: 16px;
  }
  .brand-dot { width: 112px; height: 112px; border-radius: 50%; background: var(--brand-orange); }
  .brand-name {
    color: var(--brand-blue); font-size: 20px; font-weight: 600;
    letter-spacing: 0.5px; white-space: nowrap; text-align: center;
  }
  .divider { position: absolute; left: 352px; top: 100px; width: 1px; height: 160px; background: var(--brand-orange); }
  .contact { position: absolute; left: 378px; top: 92px; }
  .person-name { font-size: 31px; font-weight: 600; color: var(--brand-blue); line-height: 1; }
  .person-name .surname { color: var(--brand-orange); }
  .person-role { font-size: 17px; color: var(--ink); margin: 6px 0 18px; }
  .contact-row { display: flex; align-items: center; gap: 10px; font-size: 17px; color: var(--ink); margin-bottom: 9px; }
  .contact-icon {
    width: 20px; height: 20px; border-radius: 50%; background: var(--brand-orange);
    display: flex; align-items: center; justify-content: center; flex: none;
  }
  .social { position: absolute; left: 450px; bottom: 28px; display: flex; gap: 18px; }
  .social-spot { width: 24px; height: 24px; border-radius: 50%; border: 2px solid var(--card-white); }
</style>
</head>
<body>
  <section class="card card-back" aria-label="Card back">
    <div class="back-mark">
      <div class="mark-dot"></div>
      <div class="mark-name">BRIGHT LANTERN STUDIO</div>
    </div>
  </section>

  <section class="card card-front" aria-label="Card front">
    <svg class="front-band" viewBox="0 0 720 412" aria-hidden="true">
      <path d="M0 404 Q 420 392 720 282 L720 412 L0 412 Z" fill="var(--brand-blue)"/>
    </svg>

    <div class="brand">
      <div class="brand-dot"></div>
      <div class="brand-name">BRIGHT LANTERN STUDIO</div>
    </div>

    <div class="divider"></div>

    <div class="contact">
      <p class="person-name">Lucien <span class="surname">MARVET</span></p>
      <p class="person-role">Founder &amp; CEO</p>
      <p class="contact-row">
        <span class="contact-icon">
          <svg width="12" height="12" viewBox="0 0 24 24"><path fill="#fff" d="M6.6 10.8a15 15 0 0 0 6.6 6.6l2.2-2.2a1 1 0 0 1 1-.25 11.4 11.4 0 0 0 3.6.57 1 1 0 0 1 1 1V20a1 1 0 0 1-1 1A17 17 0 0 1 3 4a1 1 0 0 1 1-1h3.5a1 1 0 0 1 1 1c0 1.25.2 2.45.57 3.57a1 1 0 0 1-.25 1z"/></svg>
        </span>+590 690 482 517
      </p>
      <p class="contact-row">
        <span class="contact-icon">
          <svg width="12" height="12" viewBox="0 0 24 24"><rect x="3" y="6" width="18" height="12" rx="1" fill="none" stroke="#fff" stroke-width="2"/><path d="M3 7l9 6 9-6" fill="none" stroke="#fff" stroke-width="2"/></svg>
        </span>ceo@brightlanternstudio.com
      </p>
      <p class="contact-row">
        <span class="contact-icon">
          <svg width="12" height="12" viewBox="0 0 24 24" fill="none" stroke="#fff" stroke-width="2"><circle cx="12" cy="12" r="9"/><path d="M3 12h18M12 3c3 3 3 15 0 18M12 3c-3 3-3 15 0 18"/></svg>
        </span>www.brightlanternstudio.com
      </p>
    </div>

    <div class="social" aria-label="Social channels">
      <span class="social-spot"></span>
      <span class="social-spot"></span>
      <span class="social-spot"></span>
    </div>
  </section>
</body>
</html>
```